Tessmark

We are start up and need a refresh of our pitch deck/digital brochure. images, text and overall design/feel need to be inline with our new product and website (www.tessmark.io)

Requirements
Must have
• new slide deck must match look/feel of main webpage www.tessmark,io

```html
<!DOCTYPE html>
<html lang="en">
<head>
<meta charset="utf-8">
<title>Solution</title>
<link href="https://fonts.googleapis.com/css2?family=Montserrat:wght@500;700;800&display=swap" rel="stylesheet">
<style>
  :root {
    --brand-orange: #f84e06;
    --ink: #0a0a0a;
    --paper: #ffffff;
    --device-light: #e6e6e6;
    --device-mid: #bdbdbd;
    --device-dark: #8a8a8a;
  }
  * { margin: 0; padding: 0; box-sizing: border-box; }
  html, body { width: 1200px; height: 676px; overflow: hidden; background: var(--paper); }
  body { font-family: "Montserrat", Arial, sans-serif; }
  .slide { position: relative; width: 1200px; height: 676px; background: var(--paper); }

  .title-bar { position: absolute; left: 0; top: 92px; width: 192px; height: 36px; background: var(--brand-orange); }
  .slide-title { position: absolute; left: 69px; top: 62px; font-size: 33px; font-weight: 700; color: var(--ink); letter-spacing: 0.2px; }

  .connectors { position: absolute; left: 0; top: 0; }

  .feature {
    position: absolute; width: 138px; height: 138px; border-radius: 50%;
    background: var(--brand-orange); color: var(--paper);
    display: flex; align-items: center; justify-content: center; text-align: center;
    font-size: 17.5px; font-weight: 500; line-height: 1.18; letter-spacing: 0.3px;
  }
  .feature--access { left: 32px; top: 308px; }
  .feature--organize { left: 183px; top: 193px; }
  .feature--collaborate { left: 363px; top: 193px; }
  .feature--metrics { left: 517px; top: 308px; }

  .product-device { position: absolute; left: 147px; top: 353px; width: 392px; height: 229px; }
  .product-device .device-screen {
    position: absolute; left: 37px; top: 0; width: 319px; height: 213px;
    border-radius: 8px 8px 0 0;
    background: linear-gradient(180deg, var(--device-light) 0%, var(--device-mid) 100%);
  }
  .product-device .device-base {
    position: absolute; left: 0; top: 213px; width: 392px; height: 12px;
    border-radius: 2px 2px 8px 8px;
    background: linear-gradient(180deg, #d6d6d6 0%, var(--device-dark) 100%);
  }

  .summary-panel {
    position: absolute; left: 702px; top: 194px; width: 498px; height: 383px;
    background: var(--brand-orange); padding: 78px 0 0 53px;
  }
  .summary-heading { font-size: 24px; font-weight: 800; color: var(--ink); letter-spacing: 0.3px; line-height: 1.2; }
  .summary-heading .accent { color: var(--paper); }
  .benefit-list { list-style: none; margin-top: 14px; }
  .benefit-list li {
    display: flex; align-items: center; height: 28px;
    font-size: 17.8px; font-weight: 800; color: var(--paper); letter-spacing: 0.2px;
  }
  .benefit-list svg { width: 18px; height: 15px; margin-right: 15px; flex: none; }
</style>
</head>
<body>
<main class="slide">
  <div class="title-bar"></div>
  <h1 class="slide-title">Solution</h1>

  <svg class="connectors" width="1200" height="676" aria-hidden="true">
    <g stroke="#f84e06" stroke-width="1.6">
      <line x1="268" y1="332" x2="273" y2="351"/>
      <line x1="419" y1="333" x2="415" y2="351"/>
      <line x1="168" y1="393" x2="183" y2="397"/>
      <line x1="504" y1="403" x2="520" y2="398"/>
    </g>
  </svg>

  <div class="product-device" role="img" aria-label="Laptop displaying the Tessmark briefing document with a black-and-white skyscraper photograph">
    <div class="device-screen"></div>
    <div class="device-base"></div>
  </div>

  <div class="feature feature--access">Access<br>floor plans</div>
  <div class="feature feature--organize">Organize<br>floor plans</div>
  <div class="feature feature--collaborate">Collaborate<br>internally and<br>externally</div>
  <div class="feature feature--metrics">Metrics<br>to inform<br>decisions</div>

  <section class="summary-panel">
    <h2 class="summary-heading">Big Problem, <span class="accent">Simple Solution</span></h2>
    <ul class="benefit-list">
      <li><svg viewBox="0 0 18 16"><path d="M1.5 8.5 L6.5 13.5 L16.5 2.5" fill="none" stroke="#fff" stroke-width="3.2"/></svg>Upload CAD and Strata files</li>
      <li><svg viewBox="0 0 18 16"><path d="M1.5 8.5 L6.5 13.5 L16.5 2.5" fill="none" stroke="#fff" stroke-width="3.2"/></svg>Create content library</li>
      <li><svg viewBox="0 0 18 16"><path d="M1.5 8.5 L6.5 13.5 L16.5 2.5" fill="none" stroke="#fff" stroke-width="3.2"/></svg>Access content in files</li>
      <li><svg viewBox="0 0 18 16"><path d="M1.5 8.5 L6.5 13.5 L16.5 2.5" fill="none" stroke="#fff" stroke-width="3.2"/></svg>View content on any device</li>
      <li><svg viewBox="0 0 18 16"><path d="M1.5 8.5 L6.5 13.5 L16.5 2.5" fill="none" stroke="#fff" stroke-width="3.2"/></svg>Share with collaborators</li>
      <li><svg viewBox="0 0 18 16"><path d="M1.5 8.5 L6.5 13.5 L16.5 2.5" fill="none" stroke="#fff" stroke-width="3.2"/></svg>Download files</li>
    </ul>
  </section>
</main>
</body>
</html>
```